Football field themed poster-game

I'm looking for a 22" x 29" size poster with a minimum of 300dpi, max of 300mb. File format can be jpg, gif, tiff or bmp. Would like the field portion of the poster to appear like a real grass football field. The field will need makers for each yard. I've added an addition simple clip art that shows another way for yard lines as well.The rest of the layout I would like similar, but made to look more professional. Wording should be the same as in the given draft and located in the same area or close to that area on the poster. The style is open, but should be a little minimalist in nature. Design work has to be original and cannot be taken from trademarked or copyrighted items.
Updates

Project Deadline Extended
Reason: I have 2 or 3 designs that really standout, but I would like to see just a few more.

Target Market(s)

Football fans

Font styles to use
Sans Serif

Colors

Designer to choose colors to be used in the design.

Requirements
Must have
• The design must have the same similar layout as the file I have submitted with the contest. The football field needs to be made to look like a real field with turf. boarders would be nice and a modern look.
Should not have
• hard to read fonts, changes to the major overall layout of poster.

```html
<!DOCTYPE html>
<html lang="en">
<head>
<meta charset="utf-8">
<title>Hop Huddle – Field Game Poster</title>
<link rel="stylesheet" href="https://fonts.googleapis.com/css2?family=Audiowide&display=swap">
<style>
  :root{
    --paper:#ffffff;
    --line:#ffffff;
    --turf-light:#5fb52c;
    --turf-mid:#3f9420;
    --turf-dark:#2a6e14;
    --yard-gold:#ffd21f;
    --number-gold:#f7c51e;
    --banner-gold:#ffd400;
    --banner-ink:#8c1b4a;
    --panel-hot:#e8461c;
    --panel-warm:#f79a1e;
    --panel-pale:#fdf0cf;
    --seal-gold:#d9a23a;
    --seal-deep:#a8701e;
  }
  html,body{margin:0;padding:0;overflow:hidden;background:var(--paper);}
  .poster{width:910px;height:1200px;display:block;font-family:"Audiowide",sans-serif;}
  .yard-number{font-size:31px;fill:var(--number-gold);font-family:"Audiowide",sans-serif;}
  .score-label{font-size:21px;fill:var(--paper);letter-spacing:1px;font-family:"Audiowide",sans-serif;}
  .game-title{font-size:58px;fill:var(--paper);letter-spacing:3px;font-family:"Audiowide",sans-serif;}
  .team-label{font-size:22px;fill:var(--banner-ink);font-family:"Audiowide",sans-serif;}
</style>
</head>
<body>
<svg class="poster" viewBox="0 0 910 1200" xmlns="http://www.w3.org/2000/svg">
  <defs>
    <linearGradient id="panelGradient" x1="0" y1="0" x2="0" y2="1">
      <stop offset="0" stop-color="var(--panel-hot)"/>
      <stop offset="0.15" stop-color="var(--panel-warm)"/>
      <stop offset="0.5" stop-color="var(--panel-pale)"/>
      <stop offset="0.85" stop-color="var(--panel-warm)"/>
      <stop offset="1" stop-color="var(--panel-hot)"/>
    </linearGradient>
    <radialGradient id="turfGradient" cx="0.5" cy="0.5" r="0.7">
      <stop offset="0" stop-color="var(--turf-light)"/>
      <stop offset="0.7" stop-color="var(--turf-mid)"/>
      <stop offset="1" stop-color="var(--turf-dark)"/>
    </radialGradient>
    <pattern id="yardTicks" x="0" y="0" width="50" height="18.76" patternUnits="userSpaceOnUse">
      <rect x="0" y="0" width="50" height="2" fill="var(--line)"/>
    </pattern>
  </defs>

  <!-- Score panel -->
  <g class="score-panel">
    <rect x="18" y="18" width="229" height="1165" fill="url(#panelGradient)"/>
    <g class="score-seal">
      <circle cx="123" cy="145" r="91" fill="var(--seal-deep)"/>
      <circle cx="123" cy="145" r="80" fill="var(--seal-gold)"/>
      <circle cx="123" cy="145" r="62" fill="var(--paper)"/>
    </g>
    <text class="score-label" x="123" y="270" text-anchor="middle" transform="rotate(180 123 270)" dominant-baseline="middle">SCORE</text>
    <text class="game-title" x="123" y="594" text-anchor="middle" dominant-baseline="middle" transform="rotate(90 123 594)">HOP HUDDLE</text>
    <text class="score-label" x="123" y="929" text-anchor="middle" dominant-baseline="middle">SCORE</text>
    <g class="score-seal">
      <circle cx="123" cy="1055" r="91" fill="var(--seal-deep)"/>
      <circle cx="123" cy="1055" r="80" fill="var(--seal-gold)"/>
      <circle cx="123" cy="1055" r="62" fill="var(--paper)"/>
    </g>
  </g>

  <!-- Field -->
  <g class="field">
    <rect x="260" y="18" width="632" height="1165" fill="url(#turfGradient)" role="img" aria-label="Grass turf texture"/>
    <rect x="274" y="32" width="604" height="1135" fill="none" stroke="var(--line)" stroke-width="3"/>

    <!-- corner arcs -->
    <path d="M274 64 A32 32 0 0 0 306 32" fill="none" stroke="var(--line)" stroke-width="3"/>
    <path d="M846 32 A32 32 0 0 0 878 64" fill="none" stroke="var(--line)" stroke-width="3"/>
    <path d="M274 1135 A32 32 0 0 1 306 1167" fill="none" stroke="var(--line)" stroke-width="3"/>
    <path d="M846 1167 A32 32 0 0 1 878 1135" fill="none" stroke="var(--line)" stroke-width="3"/>

    <!-- end zones -->
    <g class="end-zone end-zone--home">
      <rect x="391" y="32" width="371" height="104" fill="var(--turf-dark)" fill-opacity="0.55" stroke="var(--line)" stroke-width="3"/>
      <path d="M545 136 A32 32 0 0 0 609 136" fill="none" stroke="var(--line)" stroke-width="3"/>
      <polygon points="460,66 694,66 684,80 694,94 460,94 470,80" fill="var(--banner-gold)"/>
      <text class="team-label" x="577" y="81" text-anchor="middle" dominant-baseline="middle" transform="rotate(180 577 81)">HOME</text>
    </g>
    <g class="end-zone end-zone--visitors">
      <rect x="391" y="1067" width="371" height="100" fill="var(--turf-dark)" fill-opacity="0.55" stroke="var(--line)" stroke-width="3"/>
      <path d="M545 1067 A32 32 0 0 1 609 1067" fill="none" stroke="var(--line)" stroke-width="3"/>
      <polygon points="460,1106 694,1106 684,1120 694,1134 460,1134 470,1120" fill="var(--banner-gold)"/>
      <text class="team-label" x="577" y="1121" text-anchor="middle" dominant-baseline="middle">VISITORS</text>
    </g>

    <!-- yard ticks -->
    <g class="yard-ticks">
      <rect x="280" y="150" width="46" height="900" fill="url(#yardTicks)"/>
      <rect x="826" y="150" width="46" height="900" fill="url(#yardTicks)"/>
    </g>

    <!-- five-yard lines -->
    <g class="five-yard-lines" stroke="var(--line)" stroke-width="2">
      <line x1="276" y1="178" x2="385" y2="178"/><line x1="767" y1="178" x2="876" y2="178"/>
      <line x1="276" y1="272" x2="385" y2="272"/><line x1="767" y1="272" x2="876" y2="272"/>
      <line x1="276" y1="366" x2="385" y2="366"/><line x1="767" y1="366" x2="876" y2="366"/>
      <line x1="276" y1="459" x2="385" y2="459"/><line x1="767" y1="459" x2="876" y2="459"/>
      <line x1="276" y1="553" x2="385" y2="553"/><line x1="767" y1="553" x2="876" y2="553"/>
      <line x1="276" y1="647" x2="385" y2="647"/><line x1="767" y1="647" x2="876" y2="647"/>
      <line x1="276" y1="741" x2="385" y2="741"/><line x1="767" y1="741" x2="876" y2="741"/>
      <line x1="276" y1="835" x2="385" y2="835"/><line x1="767" y1="835" x2="876" y2="835"/>
      <line x1="276" y1="928" x2="385" y2="928"/><line x1="767" y1="928" x2="876" y2="928"/>
      <line x1="276" y1="1022" x2="385" y2="1022"/><line x1="767" y1="1022" x2="876" y2="1022"/>
    </g>

    <!-- ten-yard lines -->
    <g class="ten-yard-lines" stroke="var(--yard-gold)" stroke-width="1.5">
      <line x1="276" y1="225" x2="412" y2="225"/><line x1="740" y1="225" x2="876" y2="225"/>
      <line x1="276" y1="319" x2="412" y2="319"/><line x1="740" y1="319" x2="876" y2="319"/>
      <line x1="276" y1="412" x2="412" y2="412"/><line x1="740" y1="412" x2="876" y2="412"/>
      <line x1="276" y1="506" x2="412" y2="506"/><line x1="740" y1="506" x2="876" y2="506"/>
      <line x1="276" y1="600" x2="412" y2="600" stroke-width="4"/><line x1="740" y1="600" x2="876" y2="600" stroke-width="4"/>
      <line x1="276" y1="694" x2="412" y2="694"/><line x1="740" y1="694" x2="876" y2="694"/>
      <line x1="276" y1="788" x2="412" y2="788"/><line x1="740" y1="788" x2="876" y2="788"/>
      <line x1="276" y1="881" x2="412" y2="881"/><line x1="740" y1="881" x2="876" y2="881"/>
      <line x1="276" y1="975" x2="412" y2="975"/><line x1="740" y1="975" x2="876" y2="975"/>
    </g>

    <!-- yard numbers -->
    <g class="yard-numbers" text-anchor="middle" dominant-baseline="middle">
      <text class="yard-number" x="458" y="225">10</text>
      <text class="yard-number" x="458" y="319">20</text>
      <text class="yard-number" x="458" y="412">30</text>
      <text class="yard-number" x="458" y="506">40</text>
      <text class="yard-number" x="458" y="600">50</text>
      <text class="yard-number" x="458" y="694">40</text>
      <text class="yard-number" x="458" y="788">30</text>
      <text class="yard-number" x="458" y="881">20</text>
      <text class="yard-number" x="458" y="975">10</text>

      <text class="yard-number" x="694" y="225" transform="rotate(180 694 225)">10</text>
      <text class="yard-number" x="694" y="319" transform="rotate(180 694 319)">20</text>
      <text class="yard-number" x="694" y="412" transform="rotate(180 694 412)">30</text>
      <text class="yard-number" x="694" y="506" transform="rotate(180 694 506)">40</text>
      <text class="yard-number" x="694" y="600" transform="rotate(180 694 600)">50</text>
      <text class="yard-number" x="694" y="694" transform="rotate(180 694 694)">40</text>
      <text class="yard-number" x="694" y="788" transform="rotate(180 694 788)">30</text>
      <text class="yard-number" x="694" y="881" transform="rotate(180 694 881)">20</text>
      <text class="yard-number" x="694" y="975" transform="rotate(180 694 975)">10</text>
    </g>
  </g>
</svg>
</body>
</html>
```